依頼詳細
高級住宅地、オフィス街を対象に配るA4チラシ(片面)になります。高級感溢れるデザインをお願いいたします。
印刷はミドリカゼを使用する予定です。入稿可能なAiファイルでの作成をお願いいたします。
https://midorikaze-example.jp/dataguide/

色選びはカラーパレットをご使用ください。
記載項目
記載内容は添付のワードファイルをご参照ください。
講師プロフィール用の写真は仮の写真です。決定いたしまた方に後ほど実際に使用いただく写真をお渡しいたします。
イメージ画像を1枚添付しておりますが、使用はお任せいたします。
サイズ
A4
ページ数
片面
希望イメージ
シンプル 複雑
単色 カラフル
暗い 明るい
日常 高級
遊び心 厳粛
未来的 伝統的
女性的 男性的
希望する色
黄・オレンジ系、青系、無彩色系
納品ファイル
• イラストレーター形式 (.ai)
補足説明
当初の設定ミスで募集期間5日間としていましたが、3日間に訂正いたします。
期間が短くなりますが、どうぞよろしくお願いいたします。
報酬金額変更いたしました。
どうぞよろしくお願いいたします。
提出ファイル形式についての追記です。
採用に至った場合は、そのまま入稿できるAiファイルと後に文字を編集する予定があるためテキストをアウトライン化する前(テキスト部分が後に編集できるもの)のファイルの2種類の提出をお願いいたします。可能であればWindows Adobe Illustrator CS4対応のファイル形式でお願いします。また、特殊なフォントをご使用の場合は一緒にご提出願います。
お手数おかけいたしますがよろしくお願いいたします。

ターゲットを意識した画像の使用、レイアウト、高級感とすべてよかったです。

この度はコンペにご参加いただきありがとうございました。
予想以上に多くの提案をいただきまして大変感謝いたしております。
多数の素晴らしいご提案から選ぶのに時間がかかりまして、
お待たせいたしましたことをお詫び申し上げます。
また、機会がございましたらどうぞよろしくお願いいたします。

```html
<!DOCTYPE html>
<html lang="ja">
<head>
<meta charset="utf-8">
<title>VERAN 完全プライベート英会話レッスン</title>
<link rel="stylesheet" href="https://fonts.googleapis.com/css2?family=Noto+Serif+JP:wght@400;600;700&family=Playfair+Display:ital@1&display=swap">
<style>
:root{
  --ink:#222;
  --paper:#f4f4f2;
  --dark:#1f1f22;
  --dark2:#34343a;
  --navy:#1c2a44;
  --gold:#b8913f;
  --gold-light:#d9bd7a;
  --grey:#6a6a6a;
  --card:#efeeea;
}
*{box-sizing:border-box;margin:0;padding:0}
html,body{width:849px;height:1200px;overflow:hidden}
body{font-family:"Noto Serif JP",serif;color:var(--ink);background:var(--paper)}
.flyer{position:relative;width:849px;height:1200px;overflow:hidden;background:linear-gradient(180deg,#fafaf8 0,#e9e9e6 40%,var(--dark) 46%,#2a2a2e 100%)}
.abs{position:absolute}
.hero-photo{left:360px;top:0;width:489px;height:370px;background:linear-gradient(135deg,#cfd6de,#8b97a5 55%,#e6e8eb)}
.kicker{left:24px;top:22px;font-size:25px;line-height:1.35;font-weight:600;letter-spacing:.04em}
.brand{left:24px;top:110px;font-size:78px;font-weight:700;letter-spacing:.12em;color:var(--ink)}
.tagline{left:24px;top:222px;font-size:19px;font-weight:600;border-bottom:2px solid var(--gold);padding-bottom:6px}
.intro{left:24px;top:268px;width:330px;font-size:11.5px;line-height:1.8;color:#333}
.offer{left:372px;top:235px;width:460px;height:240px;background:#fff;border:1px solid var(--gold);box-shadow:0 2px 8px rgba(0,0,0,.15)}
.offer-tag{left:-14px;top:14px;width:52px;height:92px;background:var(--navy);color:#fff;font-size:15px;writing-mode:vertical-rl;display:flex;align-items:center;justify-content:center;letter-spacing:.2em}
.offer-time{left:56px;top:22px;font-size:18px;font-weight:700;color:var(--navy)}
.offer-badge{right:16px;top:12px;width:48px;height:48px;border-radius:50%;background:var(--navy);color:#fff;font-size:11px;display:flex;align-items:center;justify-content:center;text-align:center;line-height:1.2}
.offer-body{left:56px;top:58px;width:330px;font-size:11px;line-height:1.7;color:#333}
.offer-note{left:20px;top:148px;width:420px;font-size:11px;color:#fff;background:var(--gold);padding:4px 8px}
.offer-target{left:20px;top:182px;width:420px;text-align:center;font-size:15px;font-weight:700;color:var(--navy)}
.teacher-photo{left:14px;top:388px;width:200px;height:430px;background:linear-gradient(180deg,#5b5f66,#3b3e44 60%,#2a2c30)}
.quote{left:232px;top:520px;width:600px;font-family:"Playfair Display",serif;font-style:italic;font-size:19px;color:#fff}
.quote-ja{left:520px;top:552px;font-size:11px;color:#ddd}
.why{left:232px;top:590px;font-size:24px;font-weight:700;color:#fff;letter-spacing:.03em}
.point{width:292px;height:160px;background:var(--card);padding:14px 16px}
.point h3{font-size:14px;color:var(--navy);line-height:1.45;margin-bottom:8px;border-bottom:1px solid var(--gold);padding-bottom:6px}
.point p{font-size:10.5px;line-height:1.7;color:#333}
.name{left:14px;top:828px;font-size:16px;color:#fff;font-weight:600}
.name span{font-size:11px;color:var(--gold-light);margin-right:8px}
.profile{left:14px;top:858px;width:200px;font-size:10px;line-height:1.75;color:#ddd}
.about{left:14px;top:990px;width:200px;height:160px;background:#fff;padding:10px 12px}
.about h4{font-size:12px;color:var(--navy);margin-bottom:6px}
.about p{font-size:9.5px;line-height:1.6;color:#333}
.about .logo{margin-top:6px;font-size:18px;font-weight:700;letter-spacing:.1em;display:flex;align-items:center;gap:6px}
.about .logo i{width:10px;height:10px;background:var(--gold);display:inline-block}
.qa{width:292px;height:150px;background:#fff;padding:12px 14px}
.qa h4{font-size:12.5px;color:var(--navy);line-height:1.5;margin-bottom:6px}
.qa h4 b{color:var(--gold);font-size:18px;margin-right:6px}
.qa p{font-size:10px;line-height:1.65;color:#333}
.kid-photo{right:10px;bottom:10px;width:80px;height:90px;background:linear-gradient(180deg,#e8d9c4,#c5a98a)}
.price{left:0;top:1160px;width:849px;height:40px;background:var(--gold);color:#fff;font-size:12.5px;display:flex;align-items:center;justify-content:center;gap:24px}
.price b{background:var(--dark);padding:4px 10px}
</style>
</head>
<body>
<div class="flyer">
  <div class="abs hero-photo" role="img" aria-label="握手するビジネスマン二人の写真"></div>

  <p class="abs kicker">ワンランク上の<br>完全プライベート英会話レッスン</p>
  <h1 class="abs brand">VERAN</h1>
  <p class="abs tagline">全てにおいて最高品質を求める貴方へ</p>
  <p class="abs intro">VERANは、経営者、会社役員、議員、医師、ニュースキャスターなどエリート層向けに、妥協のない完全プライベートの英会話レッスンをご提供しています。都心の落ち着いた環境で、お客様のご要望に合わせたオーダーメイドのカリキュラムを組み、確かな成果へと導きます。</p>

  <section class="abs offer">
    <div class="abs offer-tag">限定案内</div>
    <p class="abs offer-time">火曜日 19:00〜20:00</p>
    <div class="abs offer-badge">1日<br>限定</div>
    <p class="abs offer-body">毎週火曜日の夜に体験レッスンを実施しています。講師と直接お話しいただき、レッスンの雰囲気をご確認ください。完全予約制です。</p>
    <p class="abs offer-note">週1回60分｜今回の募集枠は先着3名様までとなります</p>
    <p class="abs offer-target">対象：試験（面接・作文）通過の方</p>
  </section>

  <div class="abs teacher-photo" role="img" aria-label="講師のプロフィール写真"></div>
  <p class="abs quote">"My goal is to make the country of Japan stronger, one person at a time."</p>
  <p class="abs quote-ja">私のゴールは、一人ずつ日本をより強くすることです。</p>
  <h2 class="abs why">なぜ、ケンのレッスンはそんなに人気なのか？</h2>

  <div class="abs point" style="left:232px;top:636px">
    <h3>ケンは豊富なビジネス経験を生かした指導が可能です。</h3>
    <p>海外企業での交渉や会議の経験を持ち、実践で使える表現を丁寧にお伝えします。商談やプレゼンにすぐ役立ちます。</p>
  </div>
  <div class="abs point" style="left:540px;top:636px">
    <h3>ケンの英語レッスンは単に「英語を学ぶだけ」ではありません。</h3>
    <p>文化や考え方の違いまで理解することで、海外の相手と自然に信頼関係を築く力が身につきます。</p>
  </div>
  <div class="abs point" style="left:232px;top:808px">
    <h3>個別の課題や目標を設定します。</h3>
    <p>初回に現在の英語力と目標を確認し、お一人おひとりに合わせた学習計画を作成します。</p>
  </div>
  <div class="abs point" style="left:540px;top:808px">
    <h3>レッスンを受けるだけでは終わりません。</h3>
    <p>毎回の振り返りと課題で、次のレッスンまでの学びを着実に積み重ねていきます。</p>
  </div>

  <p class="abs name"><span>講師</span>ケン・ハーロウ</p>
  <p class="abs profile">・日本在住15年以上<br>・米国大学にて経営学を専攻<br>・外資系企業での勤務経験<br>・通訳・翻訳の実績多数<br>・経営者向け指導歴10年<br>・VERAN 代表講師</p>

  <div class="abs about">
    <h4>なぜ、英会話レッスン？</h4>
    <p>国際化が進む今、英語は必須の力です。忙しい方こそ、質の高いレッスンで効率よく学びましょう。</p>
    <p class="logo"><i></i>VERAN</p>
    <p>電話：0120-000-123<br>www.veran-english.jp</p>
  </div>

  <div class="abs qa" style="left:232px;top:990px">
    <h4><b>Q</b>レッスン会場はどちらですか？出張は可能ですか？</h4>
    <p>都内の専用教室のほか、ご自宅やオフィスへの出張レッスンにも対応しております。お気軽にご相談ください。</p>
  </div>
  <div class="abs qa" style="left:540px;top:990px">
    <h4><b>Q</b>子どものレッスンはできますか？</h4>
    <p style="width:170px">はい、小学生以上のお子様のレッスンも承っております。</p>
    <div class="abs kid-photo" role="img" aria-label="笑顔の子どもの写真"></div>
  </div>

  <div class="abs price"><b>料金</b><span>入会金 10,000円（税別）</span><span>レッスン料 20,000円／60分（税別）</span></div>
</div>
</body>
</html>
```